Electric mountain bike tours nz

We are an Electric Mountain bike tour company in New Zealand. We will be offering bike rental and guided tours around the Nelson region in New Zealand. I want our website to represent both Mountain biking and New Zealand with the colours layout and features. We want tabs for the following:
-1 about us
-2 what we offer
-3 bookings/contact
Under the about us tab will be who we are as a a company. I want the ability to add videos to each of these tabs as we move foward with videos of the tracks we will be riding. I want the website to be editable so I can add and remove videos/photos myself. Also "our bikes" will be under this tab.
Under the what we offer tab will be
-1 bike rental and pricing
-2 guided tours and pricing
-3 recommended package deals.
I want to able to put the tracks under the guided tours tab and select beginner/ intermediate/advanced and have the tracks in each of the following to match the rider level. Also to be able to have a small video of the track would be great in this section.
Bookings and contact tab
(Further information for this tab to be updated soon)
- Silver ferns, kiwi, mountains

```html
<!DOCTYPE html>
<html lang="en">
<head>
<meta charset="utf-8">
<title>VOLTRIDGE – Electric Mountain Bike Tours</title>
<link href="https://fonts.googleapis.com/css2?family=Arimo:wght@400;700&family=Bebas+Neue&display=swap" rel="stylesheet">
<style>
  :root {
    --teal-deep: #00564c;
    --teal-dark: #004d4a;
    --teal-brand: #005a4f;
    --nav-link: #3fc2c0;
    --nav-active: #d6f1ec;
    --ink: #1a1a1a;
    --mist-top: #b8c5c5;
    --white: #ffffff;
    --field: #f6fafb;
    --button: #b5c1c1;
    --dot: #3b4446;
    --fern: #012a25;
  }
  * { box-sizing: border-box; margin: 0; padding: 0; }
  html, body { width: 960px; height: 1200px; overflow: hidden; }
  body {
    position: relative;
    font-family: "Arimo", Arial, sans-serif;
    background: var(--white);
    color: var(--ink);
  }
  .abs { position: absolute; }

  /* Header + hero */
  .hero-band {
    left: 0; top: 0; width: 960px; height: 373px;
    background: var(--teal-deep);
  }
  .brand {
    left: 104px; top: 10px; height: 56px;
    display: flex; align-items: center; gap: 8px;
    color: var(--white); font-size: 15px; font-weight: 700; letter-spacing: 1px;
  }
  .brand-dot {
    width: 40px; height: 40px; border-radius: 50%;
    background: #0b2a26;
  }
  .main-nav {
    right: 116px; top: 30px;
    display: flex; gap: 23px; font-size: 17px;
  }
  .main-nav a { color: var(--nav-link); text-decoration: none; padding-bottom: 6px; }
  .main-nav a.is-active { color: var(--nav-active); border-bottom: 2px solid var(--nav-active); }
  .header-rule {
    left: 96px; top: 74px; width: 760px; height: 1px;
    background: rgba(255,255,255,0.15);
  }
  .hero-fern {
    left: 116px; top: 224px; width: 238px; height: 88px;
    border-radius: 60% 40% 60% 40% / 70% 60% 40% 30%;
    background: radial-gradient(ellipse at 60% 55%, var(--fern), rgba(1,42,37,0.85) 60%, rgba(0,86,76,0) 100%);
  }
  .hero-title {
    left: 107px; top: 148px;
    font-family: "Bebas Neue", "Arial Narrow", sans-serif;
    font-size: 42px; color: var(--white); letter-spacing: 0.5px;
  }
  .hero-tagline {
    left: 107px; top: 197px; width: 160px;
    font-size: 14px; line-height: 17px; color: var(--white);
  }
  .slide {
    left: 393px; top: 102px; width: 451px; height: 244px;
    background: linear-gradient(180deg, #9bbfd8 0%, #5f7f8a 38%, #3d5a37 60%, #7a6d4a 100%);
  }
  .slide-arrow {
    top: 197px; width: 30px; height: 53px;
    background: rgba(20,20,20,0.8);
    display: flex; align-items: center; justify-content: center;
  }
  .slide-arrow.prev { left: 393px; }
  .slide-arrow.next { left: 814px; background: rgba(20,20,20,0.35); }

  /* About */
  .mist-band {
    left: 0; top: 373px; width: 960px; height: 307px;
    background: linear-gradient(180deg, var(--mist-top) 0%, #eef1f1 45%, var(--white) 75%);
  }
  .slide-dots { left: 571px; top: 391px; display: flex; gap: 8px; }
  .slide-dots span { width: 10px; height: 10px; border-radius: 50%; background: var(--dot); }
  .slide-dots span.is-current { background: #2f8e7e; border: 2px solid var(--dot); }
  .section-rule {
    left: 104px; top: 410px; width: 751px; height: 1px;
    background: rgba(255,255,255,0.8);
  }
  .about-heading {
    left: 184px; top: 454px; width: 192px; height: 64px;
    border: 1px solid #111;
    display: flex; align-items: center; justify-content: center;
    font-size: 23px; color: var(--teal-brand); font-weight: 400;
  }
  .about-copy {
    left: 106px; top: 544px; width: 370px;
    font-size: 15.5px; line-height: 21px;
  }
  .about-visual {
    left: 582px; top: 434px; width: 220px; height: 170px;
    border-radius: 45%;
    background: radial-gradient(ellipse at 60% 55%, #9ccf3c 0%, #6ea52a 40%, #3f7d2a 70%, rgba(255,255,255,0) 100%);
  }

  /* Offers */
  .offer-icon { top: 666px; }
  .offer-label { top: 798px; font-size: 19.5px; color: var(--ink); white-space: nowrap; }

  /* Booking */
  .booking-band {
    left: 0; top: 858px; width: 960px; height: 342px;
    background: linear-gradient(135deg, #00584a 0%, #005150 100%);
  }
  .booking-title {
    left: 0; top: 875px; width: 960px; text-align: center;
    font-size: 19.5px; color: var(--white);
  }
  .field {
    left: 317px; width: 326px;
    background: var(--field); border: 1px solid #d5dede;
    font-size: 10.5px; padding: 9px 3px; color: #111;
  }
  .field.name { top: 913px; height: 38px; }
  .field.email { top: 971px; height: 38px; }
  .field.message { top: 1024px; height: 106px; }
  .send-button {
    left: 664px; top: 1102px; width: 66px; height: 28px;
    background: var(--button); color: #111; font-size: 11px;
    display: flex; align-items: center; justify-content: center;
  }
  .copyright {
    left: 0; top: 1167px; width: 960px; text-align: center;
    font-size: 14px; color: var(--white);
  }
</style>
</head>
<body>
  <header>
    <div class="abs hero-band"></div>
    <div class="abs brand"><span class="brand-dot"></span>VOLTRIDGE</div>
    <nav class="abs main-nav">
      <a href="#" class="is-active">Home</a>
      <a href="#">About Us</a>
      <a href="#">What we offer</a>
      <a href="#">Contact Us</a>
    </nav>
    <div class="abs header-rule"></div>
  </header>

  <section class="hero">
    <div class="abs hero-fern" role="img" aria-label="Silver fern decoration"></div>
    <h1 class="abs hero-title">VOLTRIDGE</h1>
    <p class="abs hero-tagline">Electric Mountain bike tour in Neson area of New-Zealand</p>
    <div class="abs slide" role="img" aria-label="Photo of an electric mountain bike on a hilltop trail overlooking the coast"></div>
    <div class="abs slide-arrow prev">
      <svg width="14" height="18" viewBox="0 0 14 18"><path d="M10 2 L4 9 L10 16" fill="none" stroke="#fff" stroke-width="3"/></svg>
    </div>
    <div class="abs slide-arrow next">
      <svg width="14" height="18" viewBox="0 0 14 18"><path d="M4 2 L10 9 L4 16" fill="none" stroke="#fff" stroke-width="3"/></svg>
    </div>
  </section>

  <section class="about">
    <div class="abs mist-band"></div>
    <div class="abs slide-dots"><span class="is-current"></span><span></span><span></span><span></span><span></span></div>
    <div class="abs section-rule"></div>
    <h2 class="abs about-heading">About Us</h2>
    <p class="abs about-copy">We are an Electric Mountain bike tour company in New Zealand. We offer bike rental and guided tours around the Nelson region in New Zealand</p>
    <div class="abs about-visual" role="img" aria-label="Kiwifruit halves with leaves"></div>
  </section>

  <section class="offers">
    <svg class="abs offer-icon" style="left:124px;top:692px" width="146" height="86" viewBox="0 0 146 86">
      <g fill="none" stroke="var(--teal-brand)" stroke-width="6" stroke-linejoin="round">
        <circle cx="29" cy="55" r="26"/>
        <circle cx="115" cy="55" r="26"/>
        <path d="M29 55 L52 15 L97 15 L115 55 M52 15 L72 55 L29 55 M72 55 L97 15"/>
        <path d="M40 4 L62 4 M88 4 L104 4 M94 4 L97 15"/>
      </g>
      <circle cx="72" cy="55" r="5" fill="var(--teal-brand)"/>
    </svg>
    <div class="abs offer-label" style="left:104px">Bike Rental and Pricing</div>

    <svg class="abs offer-icon" style="left:384px" width="100" height="112" viewBox="0 0 100 112">
      <g fill="var(--teal-brand)">
        <rect x="41" y="0" width="22" height="8"/>
        <path d="M8 14 L88 14 L100 28 L88 42 L8 42 Z M18 22 L18 34 L84 34 L90 28 L84 22 Z" fill-rule="evenodd"/>
        <rect x="41" y="42" width="8" height="12"/>
        <path d="M12 54 L92 54 L92 82 L12 82 L0 68 Z M20 62 L10 68 L20 74 L84 74 L84 62 Z" fill-rule="evenodd"/>
        <rect x="41" y="82" width="8" height="30"/>
        <rect x="41" y="104" width="22" height="8"/>
        <rect x="55" y="90" width="8" height="22"/>
      </g>
    </svg>
    <div class="abs offer-label" style="left:350px">Guided tours and Pricing</div>

    <svg class="abs offer-icon" style="left:666px;top:672px" width="116" height="104" viewBox="0 0 116 104">
      <path d="M0 0 L104 0 L104 50 L94 50 L94 10 L66 10 L66 36 L46 36 L46 10 L10 10 L10 84 L60 84 L60 94 L0 94 Z" fill="var(--teal-brand)"/>
      <rect x="20" y="66" width="22" height="8" fill="var(--teal-brand)"/>
      <circle cx="87" cy="77" r="27" fill="var(--teal-brand)"/>
      <path d="M75 77 L84 86 L100 69" fill="none" stroke="#fff" stroke-width="6"/>
    </svg>
    <div class="abs offer-label" style="left:601px">Recommended Pakage deals</div>
  </section>

  <footer>
    <div class="abs booking-band"></div>
    <h2 class="abs booking-title" style="font-weight:400">Booking/Contact</h2>
    <div class="abs field name">Name</div>
    <div class="abs field email">Email</div>
    <div class="abs field message">Message</div>
    <div class="abs send-button">SEND</div>
    <p class="abs copyright">CopyRight Reserved 2018 All Rights Reserved</p>
  </footer>
</body>
</html>
```